** Wanted ** Wordpress web design for scaffolding rental and construction company

We need a website design and must be functional to show a basic overview of what our company offers as a service. We have a domain name and a logo but we need web design. This web site should have another scaffolding rental page for construction and renovation as well as a quote section where customers can enter their personal information and also upload photos. The site% 26quot; www.corvithane.com% 26quot; should be intuitive, clear and classy ... The logo must be found on the site in several ways.

Target Market(s)

Professional and no professional

Coding

Coded - Design and coding required

Number of Pages Required

3 page

Font styles to use
Serif
Sans Serif
Decorative
Script

Requirements
Must have
• Our logo
Nice to have
• Slogan:% 26quot; The height% 26 # 224; port% 26 # 233; e hand% 26quot;

```html
<!DOCTYPE html>
<html lang="en">
<head>
<meta charset="utf-8">
<title>Corvithane — Scaffolding Rental</title>
<link href="https://fonts.googleapis.com/css2?family=Montserrat:wght@400;500;600;700&family=Gelasio:wght@700&display=swap" rel="stylesheet">
<style>
:root{
  --orange:#ef8a1d;
  --ink:#111111;
  --dark:#1f1f1f;
  --card:#2d2d2d;
  --text:#6a6a6a;
  --panel:#f7f7f7;
  --white:#ffffff;
}
*{box-sizing:border-box;margin:0;padding:0}
html,body{width:1200px;height:4615px;overflow:hidden;background:var(--white)}
body{position:relative;font-family:'Montserrat',sans-serif;color:var(--text)}
.abs{position:absolute}
.serif{font-family:'Gelasio',serif;font-weight:700}

/* brand */
.brand{display:flex;align-items:center;gap:10px;color:var(--orange);font-family:'Montserrat',sans-serif;font-weight:700;letter-spacing:2px}
.brand-square{background:var(--orange);flex:none}

/* hero */
.hero{left:0;top:0;width:1200px;height:625px;
  background:linear-gradient(180deg,#2a3442 0%,#3c3f48 35%,#8a5a36 62%,#c57a3a 72%,#2a2320 88%,#141414 100%);
  clip-path:polygon(0 0,100% 0,100% 84%,50% 100%,0 86%)}
.hero-shade{left:0;top:0;width:1200px;height:625px;background:rgba(0,0,0,.28);clip-path:polygon(0 0,100% 0,100% 84%,50% 100%,0 86%)}
.nav{top:38px;left:604px;display:flex;gap:27px;font-size:13px;color:var(--white)}
.nav .active{color:var(--orange)}
.nav-phone{display:flex;align-items:center;gap:5px}
.eyebrow{left:80px;top:184px;font-size:13px;font-weight:700;color:var(--white);letter-spacing:.5px}
.hero-title{left:80px;top:252px;font-size:35px;line-height:46px;font-weight:600;color:var(--white);width:520px}
.hero-copy{left:80px;top:364px;width:510px;font-size:12.5px;line-height:21px;color:#e6e6e6}
.btn{display:flex;align-items:center;justify-content:center;gap:12px;background:var(--ink);color:var(--white);font-size:12.5px;font-weight:600;letter-spacing:2px;border-radius:7px}
.btn-dot{width:14px;height:14px;border-radius:50%;background:var(--white);display:flex;align-items:center;justify-content:center}
.btn-dot::after{content:"";border-left:6px solid var(--ink);border-top:4px solid transparent;border-bottom:4px solid transparent;margin-left:2px}

.quote-head{left:624px;top:192px;width:490px;height:39px;background:var(--orange);color:var(--white);font-size:24px;font-weight:600;display:flex;align-items:center;justify-content:center}
.quote-note{left:614px;top:262px;width:500px;font-size:12.5px;line-height:21px;color:#eeeeee}
.field{border:1.5px solid var(--orange);color:var(--orange);font-size:12.5px;padding:10px 12px;background:rgba(0,0,0,.15)}
.file{left:1002px;top:363px;font-size:12px;color:var(--orange);display:flex;align-items:center;gap:4px;white-space:nowrap}
.file span{background:var(--white);color:#222;border:1px solid #999;padding:1px 6px;font-size:11.5px}
.send{left:614px;top:462px;width:508px;height:45px;background:var(--ink);border:1.5px solid var(--orange);color:var(--white);font-size:12.5px;font-weight:600;display:flex;align-items:center;justify-content:center}

/* who */
.who-panel{left:68px;top:782px;width:514px;height:737px;background:var(--panel)}
.bar{background:var(--orange);color:var(--white);font-weight:600;display:flex;align-items:center;letter-spacing:1.5px}
.who-bar{left:107px;top:785px;width:660px;height:53px;font-size:34px;padding-left:14px}
.photo{position:absolute}
.who-copy{left:102px;top:862px;width:443px;font-size:12.5px;line-height:20.6px;text-align:justify}
.pillar{width:220px;text-align:center}
.pillar-icon{width:90px;height:90px;border-radius:50%;background:var(--ink);margin:0 auto;display:flex;align-items:center;justify-content:center}
.pillar h3{font-size:17px;color:#222;margin-top:22px}
.pillar p{font-size:12.5px;line-height:21px;margin-top:14px}

/* products */
.products-bar{left:80px;top:1603px;width:1043px;height:54px;font-size:34px;justify-content:center}
.products-intro{left:100px;top:1680px;width:1000px;text-align:center;font-size:12.5px;line-height:21px}
.product{position:absolute;width:320px;text-align:center}
.product .pic{width:266px;height:220px;margin:0 auto}
.product h3{font-size:17px;color:#222;margin-top:20px}
.product p{font-size:12.5px;line-height:21px;margin-top:14px}

/* why */
.why{left:0;top:2620px;width:1200px;height:833px;
  background:linear-gradient(180deg,#151515 0%,#22211f 45%,#2e2a26 70%,#141414 100%);
  clip-path:polygon(0 80px,50% 0,100% 80px,100% 792px,50% 833px,0 792px)}
.why-bar{left:80px;top:2738px;width:1043px;height:52px;font-size:34px;justify-content:center}
.why-intro{left:100px;top:2816px;width:1000px;text-align:center;color:var(--white);font-size:12.5px}
.why-label{position:absolute;color:var(--white);font-size:12px;line-height:15px;text-transform:uppercase}

/* clients */
.clients-bar{left:72px;top:3578px;width:1060px;height:52px;font-size:34px;justify-content:center}
.review{position:absolute;width:323px;height:316px;background:var(--card);border-radius:4px;text-align:center;color:#e5e5e5}
.avatar{width:90px;height:90px;border-radius:50%;margin:43px auto 0;background:linear-gradient(160deg,#d7d7d7,#8b8f96 60%,#3a3f4a)}
.review p{font-size:12.5px;line-height:21px;width:270px;margin:22px auto 0}
.stars{font-size:13px;letter-spacing:1px;color:#cfcfcf;margin-top:6px}
.stars i{font-style:normal;color:#6e6e6e}
.review .name{font-size:12px;font-weight:600;color:var(--white);margin-top:10px}

/* footer */
.footer{left:0;top:4083px;width:1200px;height:532px;
  background:linear-gradient(180deg,#262626 0%,#1b1b1b 60%,#111 100%);
  clip-path:polygon(0 126px,50% 0,100% 126px,100% 100%,0 100%)}
.foot-head{color:var(--orange);font-size:16px}
.foot-links{left:103px;top:4318px;font-size:12.5px;color:var(--white);line-height:40.7px;text-transform:uppercase}
.foot-links .active{color:var(--orange)}
.foot-copy{left:320px;top:4340px;width:420px;text-align:center;font-size:12.5px;line-height:21px;color:#e5e5e5}
.social{position:absolute;top:4425px;width:32px;height:32px;border-radius:50%;background:var(--orange)}
.contact{position:absolute;left:784px;display:flex;gap:14px;color:var(--white)}
.contact-icon{width:32px;height:32px;border-radius:50%;background:var(--orange);display:flex;align-items:center;justify-content:center;flex:none}
.contact h4{font-size:16px;font-family:'Gelasio',serif;font-weight:700}
.contact span{font-size:12px;line-height:20px;display:block}
.rule{left:0;top:4549px;width:1200px;height:1px;background:#333}
.copyright{left:0;top:4574px;width:1200px;text-align:center;color:#cfcfcf;font-size:12.5px}
</style>
</head>
<body>

<!-- HERO -->
<div class="abs hero" role="img" aria-label="Photo of scaffolding and crane silhouettes against an evening sky"></div>
<div class="abs hero-shade"></div>

<div class="abs brand" style="left:28px;top:34px;font-size:17px">
  <div class="brand-square" style="width:26px;height:26px"></div>CORVITHANE
</div>

<nav class="abs nav">
  <span class="active">HOME</span><span>PRODUCTS</span><span>ABOUT</span><span>TESTIMONIES</span><span>CONTACT</span>
  <span class="nav-phone"><svg width="12" height="12" viewBox="0 0 24 24"><path d="M6.6 10.8c1.4 2.8 3.8 5.2 6.6 6.6l2.2-2.2c.3-.3.7-.4 1-.2 1.1.4 2.3.6 3.6.6.6 0 1 .4 1 1V20c0 .6-.4 1-1 1C10.6 21 3 13.4 3 4c0-.6.4-1 1-1h3.5c.6 0 1 .4 1 1 0 1.2.2 2.4.6 3.6.1.3 0 .7-.2 1z" fill="#ef8a1d"/></svg>+1-555-0142</span>
</nav>

<div class="abs eyebrow">BEST SCAFFOLDING RENTAL COMPANY</div>
<h1 class="abs hero-title">WE HELP TO STAND HIGH WITH FULL SAFETY</h1>
<p class="abs hero-copy">Lorem ipsum dolor sit amet, consectetur adipiscing elit. Ut elit tellus, luctus nec ullamcorper mattis, pulvinar dapibus leo.</p>
<div class="abs btn" style="left:80px;top:442px;width:248px;height:42px">LEARN MORE<span class="btn-dot"></span></div>

<div class="abs quote-head">GET A FREE QUOTE</div>
<p class="abs quote-note">Need a quick quote for a scaffold or swing stage job? Our sales staff would be happy to assist you.</p>
<div class="abs field" style="left:614px;top:355px;width:120px;height:37px">Name</div>
<div class="abs field" style="left:743px;top:355px;width:120px;height:37px">Email</div>
<div class="abs field" style="left:872px;top:355px;width:120px;height:37px">Phone</div>
<div class="abs file"><span>Choose File</span>No file chosen</div>
<div class="abs field" style="left:614px;top:403px;width:508px;height:47px">Message</div>
<div class="abs send">Send Message</div>

<!-- WHO WE ARE -->
<div class="abs who-panel"></div>
<div class="abs photo" style="left:627px;top:718px;width:508px;height:765px;background:linear-gradient(160deg,#6e6a64,#3b3a38 45%,#8a7a66 75%,#2b2a29);box-shadow:0 4px 18px rgba(0,0,0,.18)" role="img" aria-label="Photo of workers climbing a steel scaffold"></div>
<h2 class="abs bar who-bar">WHO WE ARE</h2>
<p class="abs who-copy">Lorem ipsum dolor sit amet, consectetur adipiscing elit. Ut elit tellus, luctus nec ullamcorper mattis, pulvinar dapibus leo.Lorem ipsum dolor sit amet, consectetur adipiscing elit. Ut elit tellus, luctus nec ullamcorper mattis, pulvinar dapibus leo.Lorem ipsum dolor sit amet, consectetur adipiscing elit. Ut elit tellus, luctus nec ullamcorper mattis, pulvinar dapibus leo.Lorem ipsum dolor sit amet, consectetur adipiscing elit. Ut elit tellus, luctus nec ullamcorper mattis, pulvinar dapibus leo.Lorem ipsum dolor sit amet, consectetur adipiscing elit. Ut elit tellus, luctus nec ullamcorper mattis, pulvinar dapibus leo.</p>

<div class="abs pillar" style="left:103px;top:1130px">
  <div class="pillar-icon"><svg width="44" height="44" viewBox="0 0 44 44"><circle cx="22" cy="22" r="18" fill="none" stroke="#fff" stroke-width="4"/><circle cx="22" cy="22" r="10" fill="none" stroke="#fff" stroke-width="4"/><circle cx="22" cy="22" r="3.5" fill="#fff"/></svg></div>
  <h3 class="serif">OUR MISSION</h3>
  <p>Lorem ipsum dolor sit amet, consectetur adipiscing elit. Ut elit tellus, luctus nec ullamcorper mattis, pulvinar dapibus leo.</p>
</div>
<div class="abs pillar" style="left:323px;top:1130px">
  <div class="pillar-icon"><svg width="40" height="44" viewBox="0 0 40 44"><path d="M20 4a13 13 0 0 0-8 23c1.5 1.3 2 2.6 2 4.5h12c0-1.9.5-3.2 2-4.5A13 13 0 0 0 20 4z" fill="none" stroke="#fff" stroke-width="3"/><path d="M15 36h10M16 40h8M17 22l3 5 3-5" fill="none" stroke="#fff" stroke-width="2.5"/></svg></div>
  <h3 class="serif">OUR VISION</h3>
  <p>Lorem ipsum dolor sit amet, consectetur adipiscing elit. Ut elit tellus, luctus nec ullamcorper mattis, pulvinar dapibus leo.</p>
</div>
<div class="abs btn" style="left:102px;top:1410px;width:249px;height:44px">LEARN MORE<span class="btn-dot"></span></div>

<!-- PRODUCTS -->
<h2 class="abs bar products-bar">OUR SCAFFOLD PRODUCTS</h2>
<p class="abs products-intro">Lorem ipsum dolor sit amet, consectetur adipiscing elit. Ut elit tellus, luctus nec ullamcorper mattis, pulvinar dapibus leo.Lorem ipsum dolor sit amet, consectetur adipiscing elit. Ut elit tellus, luctus nec ullamcorper mattis, pulvinar dapibus leo.</p>

<div class="product" style="left:90px;top:1780px">
  <div class="pic" style="background:linear-gradient(170deg,#7c8ea3,#8a6e57 50%,#4b4a48)" role="img" aria-label="Photo of a systems scaffold on a building facade"></div>
  <h3 class="serif">Systems Scaffold</h3>
  <p>Lorem ipsum dolor sit amet, consectetur adipiscing elit. Ut elit tellus, luctus nec ullamcorper mattis, pulvinar dapibus leo.</p>
</div>
<div class="product" style="left:441px;top:1780px">
  <div class="pic" style="background:linear-gradient(170deg,#aeb6bd,#7d7b74 50%,#5a5346)" role="img" aria-label="Photo of frame scaffolding around a building under construction"></div>
  <h3 class="serif">Frame Scaffolding</h3>
  <p>Lorem ipsum dolor sit amet, consectetur adipiscing elit. Ut elit tellus, luctus nec ullamcorper mattis, pulvinar dapibus leo.</p>
</div>
<div class="product" style="left:791px;top:1780px">
  <div class="pic" style="background:linear-gradient(170deg,#5a4a3a,#8b7356 50%,#3a332c)" role="img" aria-label="Photo of shoring scaffold inside a structure"></div>
  <h3 class="serif">Shoring Scaffolds</h3>
  <p>Lorem ipsum dolor sit amet, consectetur adipiscing elit. Ut elit tellus, luctus nec ullamcorper mattis, pulvinar dapibus leo.</p>
</div>
<div class="product" style="left:90px;top:2137px">
  <div class="pic" style="background:linear-gradient(170deg,#f1f1f1,#dcdcdc 55%,#bdbdbd)" role="img" aria-label="Photo of a rolling indy scaffold against a white wall"></div>
  <h3 class="serif">Indy Scaffolds</h3>
  <p>Lorem ipsum dolor sit amet, consectetur adipiscing elit. Ut elit tellus, luctus nec ullamcorper mattis, pulvinar dapibus leo.</p>
</div>
<div class="product" style="left:441px;top:2137px">
  <div class="pic" style="background:linear-gradient(170deg,#4d7fae,#c9d6e2 45%,#5f5f5f)" role="img" aria-label="Photo of a tower with swing stage and cranes under a cloudy sky"></div>
  <h3 class="serif">Swing Stage Scaffolding</h3>
  <p>Lorem ipsum dolor sit amet, consectetur adipiscing elit. Ut elit tellus, luctus nec ullamcorper mattis, pulvinar dapibus leo.</p>
</div>
<div class="product" style="left:791px;top:2137px">
  <div class="pic" style="background:linear-gradient(170deg,#c9cdd2,#6f737a 50%,#2e3036)" role="img" aria-label="Photo of steel ladders and scaffold frames seen from below"></div>
  <h3 class="serif">Ladders</h3>
  <p>Lorem ipsum dolor sit amet, consectetur adipiscing elit. Ut elit tellus, luctus nec ullamcorper mattis, pulvinar dapibus leo.</p>
</div>
<div class="abs btn" style="left:843px;top:2502px;width:248px;height:43px">LEARN MORE<span class="btn-dot"></span></div>

<!-- WHY -->
<div class="abs why" role="img" aria-label="Dark photo of a construction site at dusk"></div>
<h2 class="abs bar why-bar">WHY CHOSE CORVITHANE</h2>
<p class="abs why-intro">Lorem ipsum dolor sit amet, consectetur adipiscing elit. Ut elit tellus, luctus nec ullamcorper mattis, pulvinar dapibus leo.</p>

<svg class="abs" style="left:0;top:2620px" width="1200" height="833" viewBox="0 0 1200 833">
  <g fill="none" stroke="#ef8a1d" stroke-width="1.5">
    <circle cx="577" cy="500" r="158" stroke-dasharray="120 60" opacity=".9"/>
    <path d="M530 371 L470 332 L433 332"/>
    <path d="M442 500 L399 500"/>
    <path d="M530 629 L470 668 L433 668"/>
    <path d="M627 371 L687 332 L724 332"/>
    <path d="M716 500 L758 500"/>
    <path d="M627 629 L687 668 L724 668"/>
  </g>
  <g fill="none" stroke="#ffffff" stroke-width="2.5">
    <path d="M530 371 A136 136 0 0 0 530 629"/>
    <path d="M627 371 A136 136 0 0 1 627 629"/>
  </g>
  <g fill="#fff" stroke="#ef8a1d" stroke-width="2">
    <circle cx="530" cy="371" r="9"/><circle cx="442" cy="500" r="9"/><circle cx="530" cy="629" r="9"/>
    <circle cx="627" cy="371" r="9"/><circle cx="716" cy="500" r="9"/><circle cx="627" cy="629" r="9"/>
  </g>
  <g fill="#1b1b1b" stroke="#ef8a1d" stroke-width="2">
    <circle cx="401" cy="332" r="32"/><circle cx="367" cy="500" r="32"/><circle cx="401" cy="668" r="32"/>
    <circle cx="756" cy="332" r="32"/><circle cx="790" cy="500" r="32"/><circle cx="756" cy="668" r="32"/>
  </g>
  <g fill="none" stroke="#fff" stroke-width="2" stroke-linecap="round" stroke-linejoin="round">
    <circle cx="401" cy="322" r="7"/><path d="M387 346c2-8 7-12 14-12s12 4 14 12"/>
    <path d="M367 484l13 5v10c0 8-6 13-13 16-7-3-13-8-13-16v-10z"/><path d="M361 500l4 4 8-8"/>
    <circle cx="401" cy="668" r="13"/><path d="M405 662h-6a3 3 0 0 0 0 6h4a3 3 0 0 1 0 6h-6M401 658v20"/>
    <rect x="742" y="318" width="28" height="20" rx="2"/><path d="M750 346h12M756 338v8"/>
    <circle cx="790" cy="500" r="14"/><path d="M790 491v9l6 5"/>
    <circle cx="756" cy="662" r="10"/><path d="M749 670l-4 12 6-3 4 5 2-9M763 670l4 12-6-3-4 5"/><path d="M752 662l3 3 5-6"/>
  </g>
</svg>
<div class="abs brand" style="left:488px;top:3136px;font-size:20px;color:var(--orange)">
  <div class="brand-square" style="width:20px;height:20px"></div>CORVITHANE
</div>

<div class="why-label" style="left:245px;top:2930px;width:120px">Professional and trained employees</div>
<div class="why-label" style="left:245px;top:3106px;width:95px">Safety is paramount to us</div>
<div class="why-label" style="left:255px;top:3275px;width:80px">No hidden fees</div>
<div class="why-label" style="left:799px;top:2938px;width:140px">We offer a free consultation</div>
<div class="why-label" style="left:830px;top:3106px;width:150px">All inclusive flat and hourly rates</div>
<div class="why-label" style="left:797px;top:3266px;width:110px">We've got an excellent reputation</div>

<!-- CLIENTS -->
<h2 class="abs bar clients-bar">WHAT OUR CLIENTS SAY</h2>
<div class="review" style="left:84px;top:3673px">
  <div class="avatar" role="img" aria-label="Portrait photo of the client"></div>
  <p>Elit tellus, luctus nec ullamcorper mattis, pulvinar dapibus leo. Nam varius consectet.</p>
  <div class="stars">★★★★<i>★</i></div>
  <div class="name">Nora Halvey</div>
</div>
<div class="review" style="left:441px;top:3700px">
  <div class="avatar" role="img" aria-label="Portrait photo of the client"></div>
  <p>Elit tellus, luctus nec ullamcorper mattis, pulvinar dapibus leo. Nam varius consectetur.</p>
  <div class="stars">★★★★<i>★</i></div>
  <div class="name">Evan Tull</div>
</div>
<div class="review" style="left:797px;top:3673px">
  <div class="avatar" role="img" aria-label="Portrait photo of the client"></div>
  <p>Elit tellus, luctus nec ullamcorper mattis, pulvinar dapibus leo. Nam varius consectetur elem.</p>
  <div class="stars">★★★★<i>★</i></div>
  <div class="name">Greta Lowell</div>
</div>

<!-- FOOTER -->
<div class="abs footer" role="img" aria-label="Dark photo of a building site behind the footer"></div>
<h4 class="abs foot-head serif" style="left:84px;top:4240px">NAVIGATION</h4>
<div class="abs foot-links">
  <div class="active">Home</div><div>Products</div><div>About</div><div>Testimonies</div><div>Contact</div>
</div>

<div class="abs brand" style="left:415px;top:4276px;font-size:26px">
  <div class="brand-square" style="width:28px;height:28px"></div>CORVITHANE
</div>
<p class="abs foot-copy">Lorem ipsum dolor sit amet, consectetur adipiscing elit. Ut elit tellus, luctus nec ullamcorper mattis, pulvinar dapibus leo.</p>
<div class="social" style="left:430px"></div>
<div class="social" style="left:478px"></div>
<div class="social" style="left:527px"></div>
<div class="social" style="left:577px"></div>
<div class="social" style="left:625px"></div>

<h4 class="abs foot-head serif" style="left:783px;top:4232px">GET IN TOUCH</h4>
<div class="contact" style="top:4296px">
  <div class="contact-icon"><svg width="14" height="14" viewBox="0 0 24 24"><path d="M6.6 10.8c1.4 2.8 3.8 5.2 6.6 6.6l2.2-2.2c.3-.3.7-.4 1-.2 1.1.4 2.3.6 3.6.6.6 0 1 .4 1 1V20c0 .6-.4 1-1 1C10.6 21 3 13.4 3 4c0-.6.4-1 1-1h3.5c.6 0 1 .4 1 1 0 1.2.2 2.4.6 3.6.1.3 0 .7-.2 1z" fill="#fff"/></svg></div>
  <div><h4>Call Us</h4><span>+1 555 0142</span></div>
</div>
<div class="contact" style="top:4358px">
  <div class="contact-icon"><svg width="14" height="12" viewBox="0 0 24 20"><rect x="1" y="1" width="22" height="18" rx="2" fill="none" stroke="#fff" stroke-width="2.5"/><path d="M2 3l10 8 10-8" fill="none" stroke="#fff" stroke-width="2.5"/></svg></div>
  <div><h4>Email Us</h4><span>contact@example.com</span></div>
</div>
<div class="contact" style="top:4420px">
  <div class="contact-icon"><svg width="12" height="16" viewBox="0 0 18 24"><path d="M9 1a8 8 0 0 0-8 8c0 6 8 14 8 14s8-8 8-14a8 8 0 0 0-8-8z" fill="#fff"/><circle cx="9" cy="9" r="3" fill="#ef8a1d"/></svg></div>
  <div><h4>Address</h4><span>48 Harbor Row, Lane no 9,<br>Westbrook WB20417</span></div>
</div>

<div class="abs rule"></div>
<div class="abs copyright">Copyright © 2020 corvithane</div>

</body>
</html>
```